Construction Machinery Company : needs two pages flyers to advertise "Demolition Tools"

>>UPDATE BRIEF

Hi Mr./ Ms, Designers,

To make your design work easier,
- I have updated the instruction (Please see attachment file 5 "Brief" , or below "Requirement session")
- I also re-upload the attachments. They are all photos and content for the design. Very Clear now.
- I have also increased the budget.

*More information, please go
www.tarnvale-works.com/spikeline

Hope you can work on my project.

>>Previous Brief
Hi Mr./ Ms. Designers,

We are an international construction machinery distributors, located in Hong Kong. Our client is HONG KONG contractors.
We want to start marketing "demolition tool" - the metal tool that used on excavator breaker.

We want the final designs export to two products
1) two pages A4 size flyers (Front for products, and Back for company info.)
2) one page 360mm x 265mm size advertisement (grouping products and company information together)
* design can be the same.

Requirement:
1) Tone: As construction industry is a very "man" industry, we want the flyer is very "METAL" theme.
(Our Company theme colour is RED, but you can use a new colour"

2) Theme: I want customer know we are PROFESSIONAL, SPECIALIST moil point seller, and we have a lot of experience.

3) Product message: we want the messages are
-TOUGHER,
-LONGER LIFE,
-LOWER PRICE,
-CONVENIENCE DELIVERY

4) Product: there are four kinds of "demolition tool", Moil Point, Wedge, Blunt, Cone. But I want to emphasis "Moil Point".

Remarks:
- To let you know what demolition tool is,
I have attached photos [teaching] for your reference.

- Beside the Product photos, we may put supplier's factory photos as background, to show it is a big factory.

- I have put many photo, as Source and for Reference.
Feel free to ask me questions.

- We may put "Chinese word" beside English in the end. I can send you the FONT file later.

Our website page:
http://tarnvale-works.com/spikeline/

Learning Reference:
http://www.quorbinrigs.com/tools-parts.html

Target Market(s)

[Hong Kong] Construction Contractor user.

Industry/Entity Type

Construction Company

Requirements
Must have
• Theme: Since construction is a very "man" industry, Please have the theme "man and neat"
• two pages A4 size flyers

```html
<!DOCTYPE html>
<html lang="en">
<head>
<meta charset="utf-8">
<title>Tarnvale Works – Demolition Tools Flyer</title>
<link rel="stylesheet" href="https://fonts.googleapis.com/css2?family=Lato:wght@400;700&family=Roboto+Condensed:wght@700&family=Noto+Sans+TC:wght@400;500&display=swap">
<style>
  :root {
    --red: #e3202a;
    --red-dark: #b8141c;
    --red-deep: #9c0f16;
    --charcoal: #1c1c1e;
    --charcoal-2: #2b2b2e;
    --strip: #3a3a3c;
    --silver: #c9ccd1;
    --ink: #333333;
    --white: #ffffff;
    --stage: #e6e4e1;
  }
  * { box-sizing: border-box; margin: 0; padding: 0; }
  html, body { width: 1200px; height: 900px; overflow: hidden; }
  body {
    background: var(--stage);
    font-family: "Lato", Arial, sans-serif;
    position: relative;
  }
  .page {
    position: absolute;
    top: 54px;
    width: 560px;
    height: 792px;
    overflow: hidden;
    box-shadow: 0 6px 18px rgba(0,0,0,.25);
  }
  .page--front { left: 30px; background: var(--white); }
  .page--back { left: 610px; background: linear-gradient(180deg, var(--charcoal-2) 0%, var(--charcoal) 60%, #141416 100%); }

  /* ---------- front: hero ---------- */
  .hero { position: absolute; left: 0; top: 0; width: 560px; height: 350px; }
  .hero svg { display: block; }
  .brand-mark {
    position: absolute; left: 0; top: 272px; width: 560px;
    display: flex; align-items: center; justify-content: center; gap: 10px;
  }
  .brand-mark__dot { width: 14px; height: 14px; border-radius: 50%; background: var(--white); }
  .brand-mark__name {
    font-family: "Roboto Condensed", "Arial Narrow", sans-serif;
    font-weight: 700; font-size: 34px; color: var(--white); letter-spacing: 1px;
  }
  .company-title {
    position: absolute; top: 352px; left: 0; width: 560px; text-align: center;
    font-family: "Roboto Condensed", "Arial Narrow", sans-serif;
    font-weight: 700; font-size: 30px; color: var(--red); letter-spacing: .5px;
  }

  /* ---------- front: benefits ---------- */
  .benefits { position: absolute; top: 392px; left: 20px; width: 520px; display: flex; justify-content: space-between; }
  .benefit { width: 165px; text-align: center; position: relative; }
  .benefit--featured::before {
    content: ""; position: absolute; left: 0; top: -8px; width: 165px; height: 150px;
    background: #ececec; z-index: 0;
  }
  .benefit__photo {
    position: relative; z-index: 1;
    width: 104px; height: 104px; border-radius: 50%; margin: 0 auto;
    border: 3px solid var(--white); box-shadow: 0 1px 4px rgba(0,0,0,.3);
  }
  .benefit__photo--factory { background: radial-gradient(circle at 40% 40%, #9aa3ab, #4e5a63); }
  .benefit__photo--product { background: radial-gradient(circle at 50% 40%, #f08a5a, #c2401e); }
  .benefit__photo--stock { background: radial-gradient(circle at 45% 45%, #b9c0c4, #6d7479); }
  .benefit__badge {
    position: absolute; z-index: 2; top: 4px; left: 22px;
    width: 24px; height: 24px; border-radius: 50%;
    background: var(--red); color: var(--white);
    font-size: 11px; font-weight: 700; line-height: 24px; text-align: center;
  }
  .benefit__title {
    position: relative; z-index: 1;
    margin-top: 12px;
    font-family: "Roboto Condensed", "Arial Narrow", sans-serif;
    font-weight: 700; font-size: 13px; line-height: 15px; color: var(--red); text-transform: uppercase;
  }
  .benefit__text { position: relative; z-index: 1; margin-top: 4px; font-size: 11px; line-height: 13px; color: var(--ink); }
  .benefit__zh {
    position: relative; z-index: 1; margin-top: 10px;
    font-family: "Noto Sans TC", sans-serif; font-size: 10.5px; color: var(--red);
  }

  /* ---------- footer (shared) ---------- */
  .footer { position: absolute; left: 0; width: 560px; }
  .page--front .footer { top: 652px; height: 140px; }
  .page--back .footer { top: 640px; height: 152px; }
  .footer svg { position: absolute; left: 0; top: 0; }
  .footer__contacts {
    position: absolute; left: 0; bottom: 22px; width: 560px;
    display: flex; justify-content: space-around;
    color: var(--white); font-size: 11px; line-height: 13px;
  }
  .footer__item { width: 170px; text-align: center; }

  /* ---------- back ---------- */
  .story { position: absolute; left: 26px; top: 34px; width: 270px; }
  .story__zh {
    font-family: "Noto Sans TC", sans-serif; font-size: 12px; line-height: 17px; color: var(--red);
  }
  .story__en { margin: 12px 0 26px; font-size: 12.5px; line-height: 17px; color: var(--white); }
  .gallery { position: absolute; left: 314px; top: 24px; width: 222px; }
  .gallery__photo {
    width: 222px; height: 158px; margin-bottom: 22px;
    border: 5px solid var(--red); box-shadow: 0 4px 10px rgba(0,0,0,.6);
  }
  .gallery__photo--floor { background: linear-gradient(160deg, #a6adb3, #5f6a72 60%, #3d464c); }
  .gallery__photo--bars { background: linear-gradient(180deg, #b5b9bd, #777d82 55%, #4a4f53); }
  .gallery__photo--furnace { background: linear-gradient(170deg, #c4c8cc, #8a9094 50%, #575c60); }
  .back-band { position: absolute; left: 0; top: 604px; width: 560px; height: 40px; }
</style>
</head>
<body>

<!-- FRONT PAGE -->
<section class="page page--front">
  <div class="hero">
    <svg width="560" height="350" viewBox="0 0 560 350">
      <defs>
        <linearGradient id="heroPhoto" x1="0" y1="0" x2="0" y2="1">
          <stop offset="0" stop-color="#8e969c"/>
          <stop offset=".45" stop-color="#4b5257"/>
          <stop offset="1" stop-color="#24282b"/>
        </linearGradient>
      </defs>
      <rect width="560" height="350" fill="url(#heroPhoto)" role="img" aria-label="Factory warehouse stacked with rows of steel moil point tools"/>
      <path d="M452,0 C548,110 530,270 300,318 L0,330 L0,350 L560,350 L560,0 Z" fill="var(--red)"/>
      <path d="M474,0 C566,120 548,280 360,330" fill="none" stroke="var(--silver)" stroke-width="5"/>
      <path d="M492,0 C580,120 560,290 400,340" fill="none" stroke="#8f9399" stroke-width="2"/>
      <path d="M0,330 L300,318 C330,312 350,308 370,302 L370,350 L0,350 Z" fill="var(--red-dark)" opacity=".35"/>
      <rect y="338" width="560" height="12" fill="var(--white)"/>
    </svg>
  </div>
  <div class="brand-mark">
    <span class="brand-mark__dot"></span>
    <span class="brand-mark__name">TARNVALE</span>
  </div>
  <h1 class="company-title">TARNVALE WORKS</h1>

  <div class="benefits">
    <div class="benefit">
      <div class="benefit__photo benefit__photo--factory" role="img" aria-label="Korean production factory floor"></div>
      <span class="benefit__badge">01</span>
      <h2 class="benefit__title">Lower<br>Price</h2>
      <p class="benefit__text">Import from Korea<br>Production Factory</p>
      <p class="benefit__zh">價錢相宜 - 韓國釺杆制造廠直送</p>
    </div>
    <div class="benefit benefit--featured">
      <div class="benefit__photo benefit__photo--product" role="img" aria-label="Bundle of moil points packed for shipping"></div>
      <span class="benefit__badge">02</span>
      <h2 class="benefit__title">Longer<br>Life</h2>
      <p class="benefit__text">Superior-grade alloy steel<br>multistage tempering</p>
      <p class="benefit__zh">壽命更長 - 頂級合金鋼, 多重回火處理</p>
    </div>
    <div class="benefit">
      <div class="benefit__photo benefit__photo--stock" role="img" aria-label="Finished steel bars ready for delivery"></div>
      <span class="benefit__badge">03</span>
      <h2 class="benefit__title">Convenience<br>Delivery</h2>
      <p class="benefit__text">We will send to your job site</p>
      <p class="benefit__zh">方便客戶 - 我們會送到貴司工地</p>
    </div>
  </div>

  <footer class="footer">
    <svg width="560" height="140" viewBox="0 0 560 140">
      <rect y="0" width="560" height="20" fill="var(--strip)"/>
      <rect y="20" width="560" height="120" fill="var(--red)"/>
      <path d="M62,20 L128,20 L118,56 L72,56 Z" fill="var(--red-dark)"/>
      <path d="M247,20 L313,20 L303,56 L257,56 Z" fill="var(--red-dark)"/>
      <path d="M432,20 L498,20 L488,56 L442,56 Z" fill="var(--red-dark)"/>
      <g fill="var(--white)">
        <path d="M85,36 q10,-8 20,0 l-2,4 h-4 v-2 h-8 v2 h-4 Z M86,42 h18 v8 h-18 Z"/>
      </g>
      <g fill="none" stroke="var(--white)" stroke-width="1.6">
        <circle cx="280" cy="38" r="9"/>
        <ellipse cx="280" cy="38" rx="4" ry="9"/>
        <line x1="271" y1="38" x2="289" y2="38"/>
      </g>
      <path d="M465,29 a7,7 0 0 1 7,7 c0,5 -7,12 -7,12 c0,0 -7,-7 -7,-12 a7,7 0 0 1 7,-7 Z M465,33 a3,3 0 1 0 0.01,0 Z" fill="var(--white)" fill-rule="evenodd"/>
    </svg>
    <div class="footer__contacts">
      <p class="footer__item">+000 - 1234 - 5678<br>+000 - 1234 - 5679</p>
      <p class="footer__item">admin@tarnvale-works.com<br>tarnvale-works.com</p>
      <p class="footer__item">0000 Anywhere, Somewhere<br>Anywhere-0000</p>
    </div>
  </footer>
</section>

<!-- BACK PAGE -->
<section class="page page--back">
  <div class="story">
    <p class="story__zh">1. 我們與韓國其中一家最大的釺杆制造廠合作。制造廠每月生產5萬枝釺杆，並出口至全世界。因此我們能以最優惠價錢回饋客戶。</p>
    <p class="story__en">We operate with one of the biggest hammer tool factories in Korea. Factory produces 50,000 moil points per month and exports them worldwide. Therefore, price is always attractive to customers.</p>
    <p class="story__zh">2. 我們堅持使用頂級鋼合金料。我們擁有先進的熱處理設施，進行多重回火工序。並會仔細地檢查制成品，保證每枝釺都是高硬度及高韌性的產品。</p>
    <p class="story__en">We insist in using superior-grade of alloy steel to keep good reputation. We have advanced heat treatment facilities for multistage tempering procedure, plus carefully checks the finished tools, so that we can guarantee excellent strength and high toughness moil point.</p>
    <p class="story__zh">3. 下訂時只需提供您需要的釺杆資料，我們便會將產品送往貴司工地。</p>
    <p class="story__en">When placing your order, simply provide information of the moil points you need, and we will deliver them right at your jobsite</p>
  </div>

  <div class="gallery">
    <div class="gallery__photo gallery__photo--floor" role="img" aria-label="Overhead view of the factory machining floor"></div>
    <div class="gallery__photo gallery__photo--bars" role="img" aria-label="Steel bar stock stacked upright in the workshop"></div>
    <div class="gallery__photo gallery__photo--furnace" role="img" aria-label="Heat treatment furnaces with finished tools"></div>
  </div>

  <svg class="back-band" width="560" height="40" viewBox="0 0 560 40">
    <path d="M0,10 L560,0 L560,40 L0,40 Z" fill="#4a4a4d"/>
    <path d="M0,22 L560,14 L560,40 L0,40 Z" fill="var(--strip)"/>
  </svg>

  <footer class="footer">
    <svg width="560" height="152" viewBox="0 0 560 152">
      <rect y="0" width="560" height="152" fill="var(--red)"/>
      <path d="M62,0 L128,0 L118,40 L72,40 Z" fill="var(--red-dark)"/>
      <path d="M247,0 L313,0 L303,40 L257,40 Z" fill="var(--red-dark)"/>
      <path d="M432,0 L498,0 L488,40 L442,40 Z" fill="var(--red-dark)"/>
      <g fill="var(--white)">
        <path d="M85,16 q10,-8 20,0 l-2,4 h-4 v-2 h-8 v2 h-4 Z M86,22 h18 v8 h-18 Z"/>
      </g>
      <g fill="none" stroke="var(--white)" stroke-width="1.6">
        <circle cx="280" cy="19" r="9"/>
        <ellipse cx="280" cy="19" rx="4" ry="9"/>
        <line x1="271" y1="19" x2="289" y2="19"/>
      </g>
      <path d="M465,9 a7,7 0 0 1 7,7 c0,5 -7,12 -7,12 c0,0 -7,-7 -7,-12 a7,7 0 0 1 7,-7 Z M465,13 a3,3 0 1 0 0.01,0 Z" fill="var(--white)" fill-rule="evenodd"/>
    </svg>
    <div class="footer__contacts">
      <p class="footer__item">+000 - 1234 - 5678<br>+000 - 1234 - 5679</p>
      <p class="footer__item">admin@tarnvale-works.com<br>tarnvale-works.com</p>
      <p class="footer__item">0000 Anywhere, Somewhere<br>Anywhere-0000</p>
    </div>
  </footer>
</section>

</body>
</html>
```